Meadow Voyages Web Page Redesign

IF YOu ARE IN INDIA - PLEASE PLEASE PLEASE - make sure you are working off of MEADOWVOYAGES.COM - Not another site. Look at the URL above when you see the site!

Our website http://www.meadowvoyages.com is driven by a backend database providing content. We are interested in redesigning the website layout to make it responsive and also to make it more interesting, catchy and call to action oriented. Right now it seems not to be able to deliver the message and a little crowded. The main template pages to be addressed are index.aspx, default.aspx, TourList1.aspx, and the actual tour detail page.

There needs to be tight integration / prominent visibility for Social Media.

Focus needs to be on design that would reduce the bounce rate and be SEO friendly.

You will be responsible for layout and delivering the front end css / layout / slices to integrate with the back end.
Updates

If you are based in India, you are probably going to be redirected to another site. Please make sure you are working off of MEADOWVOYAGES.COM

Target Market(s)

It is a B2C site - travelers who are interested in traveling to India, Europe and South Africa.

Industry/Entity Type

Media

Font styles to use
Sans Serif

Requirements
Must have
• ONE VERY IMPORTANT POINT : We have a number of photographs that we would love to put online. Unfortunately our current design requires us to resize / crop the photographs which make them lose the impact. We would prefer a design where the images could be used as-is.

Tight integration with Social Media is there in our engine so it should be visible on the website.

Responsive.
Nice to have
• Try using the same color scheme but we are open for changes in the same tone..

```html
<!DOCTYPE html>
<html lang="en">
<head>
<meta charset="utf-8">
<title>Meadow Voyages</title>
<link rel="stylesheet" href="https://fonts.googleapis.com/css2?family=Mulish:wght@400;600;700&family=Open+Sans:ital,wght@0,400;0,600;1,400&family=Crimson+Text:wght@600;700&display=swap">
<style>
:root{
  --red:#a10f12;
  --red-deep:#8a0c0e;
  --red-label:#d8303a;
  --text-red:#c0262d;
  --gold:#d89b2b;
  --nav-top:#fff3d6;
  --nav-bottom:#f5d58d;
  --nav-text:#5a0f0f;
  --ink:#1d1d1d;
  --grey:#5f5f5f;
  --grey-light:#7a7a7a;
  --rule:#dcdcdc;
  --footer:#fbe3b8;
  --footer-base:#fdf1dc;
  --white:#ffffff;
}
*{box-sizing:border-box;margin:0;padding:0}
html,body{width:820px;height:1200px;overflow:hidden;background:var(--white)}
body{position:relative;font-family:"Open Sans",Arial,sans-serif;color:var(--grey)}
.abs{position:absolute}

/* header */
.site-header{left:0;top:0;width:820px;height:80px;background:var(--red)}
.brand{left:76px;top:25px;display:flex;align-items:center;gap:10px}
.brand-mark{width:30px;height:30px;border-radius:50%;background:#d9a441}
.brand-name{font-family:"Crimson Text",Georgia,serif;font-weight:700;font-size:25px;letter-spacing:.5px;color:#f3e6d2}
.tollfree{right:67px;top:31px;text-align:right;color:var(--white)}
.tollfree-label{font-family:"Mulish",sans-serif;font-size:10px}
.tollfree-number{font-family:"Mulish",sans-serif;font-weight:700;font-size:18px;margin-top:1px}

/* nav */
.main-nav{left:0;top:80px;width:820px;height:38px;background:linear-gradient(var(--nav-top),var(--nav-bottom));display:flex;padding-left:60px;box-shadow:0 1px 2px rgba(0,0,0,.15)}
.main-nav a{font-family:"Mulish",sans-serif;font-weight:600;font-size:11px;color:var(--nav-text);text-decoration:none;line-height:38px;padding:0 16px;border-right:1px solid #e2bd73}
.main-nav a:last-child{border-right:none}

/* hero */
.hero{left:0;top:118px;width:820px;height:320px;background:linear-gradient(135deg,#b8a488 0%,#d9cdbb 30%,#c9a48e 50%,#e8eef5 75%,#cfdcea 100%)}
.hero-title{left:0;top:124px;width:820px;text-align:center;font-family:"Mulish",sans-serif;font-weight:600;font-size:30px;color:var(--white);text-shadow:0 1px 3px rgba(0,0,0,.35)}
.hero-sub{left:0;top:168px;width:820px;text-align:center;font-family:"Mulish",sans-serif;font-weight:600;font-size:16px;color:var(--white);text-shadow:0 1px 3px rgba(0,0,0,.35)}
.hero-dots{left:374px;top:296px;width:72px;height:24px;border-radius:12px 12px 0 0;background:rgba(240,220,180,.85);display:flex;justify-content:center;align-items:center;gap:3px}
.hero-dots span{width:9px;height:9px;border-radius:50%;background:var(--white)}
.hero-dots span.is-active{background:var(--red)}

/* destinations */
.destination{top:453px;width:168px;height:125px;border-radius:3px;overflow:hidden}
.destination-photo{height:93px}
.destination-label{height:32px;background:var(--red-label);color:var(--white);font-family:"Crimson Text",Georgia,serif;font-weight:600;font-size:15px;letter-spacing:.6px;text-align:center;line-height:32px}

/* welcome */
.welcome{left:67px;top:626px;width:450px}
.welcome h1{font-family:"Mulish",sans-serif;font-weight:400;font-size:21px;color:var(--ink)}
.welcome-lead{font-size:11.5px;line-height:15px;color:var(--grey);margin-top:9px}
.welcome-body{font-size:9.4px;line-height:14.6px;color:var(--grey);margin-top:9px}

.deals{left:539px;top:628px;width:215px}
.deals h2{font-family:"Mulish",sans-serif;font-weight:400;font-size:18px;color:var(--gold)}
.deals-link{font-size:11px;line-height:15px;color:var(--text-red);margin-top:4px}
.deals-text{font-size:9px;line-height:13.6px;color:var(--grey-light);margin-top:4px}
.button-gold{display:inline-block;margin-top:9px;width:84px;height:24px;border-radius:3px;background:linear-gradient(#eab85c,#d19428);color:var(--white);font-family:"Mulish",sans-serif;font-weight:600;font-size:9.5px;text-align:center;line-height:24px}

.divider{left:65px;top:795px;width:690px;height:1px;background:var(--rule)}

/* testimonials */
.testimonials-title{left:67px;top:815px;font-family:"Mulish",sans-serif;font-weight:400;font-size:20px;color:var(--text-red)}
.avatar{width:62px;height:62px;border-radius:50%;background:linear-gradient(#cfc2b6,#9c8a7c);box-shadow:0 4px 5px -3px rgba(0,0,0,.3)}
.quote{width:250px;font-style:italic;font-size:9.6px;line-height:15.6px;color:var(--grey)}
.quote-mark{font-family:Georgia,serif;font-style:normal;font-size:20px;color:#9a9a9a;line-height:0;position:relative;top:5px}
.quote-author{font-size:10.5px;color:var(--ink);margin-top:6px;font-style:normal}

/* footer */
.site-footer{left:0;top:979px;width:820px;height:173px;background:linear-gradient(#fde9c4,var(--footer));border-top:1px solid #f0d9ad}
.footer-col{top:1006px}
.footer-col h3{font-family:"Mulish",sans-serif;font-weight:400;font-size:15px;color:var(--red)}
.footer-col ul{list-style:none;margin-top:6px}
.footer-col li{font-size:9.3px;line-height:16.2px;color:var(--text-red)}
.newsletter-note{font-size:9.3px;color:var(--text-red);margin-top:6px}
.newsletter-input{margin-top:6px;width:156px;height:21px;background:#fdf6e8;border:1px solid #efdcb8;font-size:8px;color:#8a8a8a;padding-left:8px;line-height:19px}
.button-red{margin-top:6px;width:83px;height:23px;border-radius:2px;background:var(--red);color:var(--white);font-family:"Mulish",sans-serif;font-weight:700;font-size:10px;text-align:center;line-height:23px}
.social{display:flex;gap:6px;margin-top:8px}
.social span{width:14px;height:14px;border-radius:2px}
.social .s-one{background:#3b5b99}
.social .s-two{background:#4fb6e6}
.social .s-three{background:#1f77b0}
.social .s-four{background:#f0861c}

.footer-base{left:0;top:1152px;width:820px;height:48px;background:var(--footer-base)}
.copyright{left:67px;top:1170px;font-size:8.8px;color:#4a4a4a}
</style>
</head>
<body>

<header class="site-header abs">
  <div class="brand abs"><span class="brand-mark"></span><span class="brand-name">MEADOW VOYAGES</span></div>
  <div class="tollfree abs">
    <div class="tollfree-label">Toll Free from US &amp; Canada</div>
    <div class="tollfree-number">800.555.0142</div>
  </div>
</header>

<nav class="main-nav abs">
  <a>HOME</a><a>ABOUT US</a><a>TOUR CALENDER</a><a>AFRICA</a><a>BUY TRAVEL INSURANCE</a><a>MY ACCOUNT</a><a>CONTACT US</a>
</nav>

<section class="hero abs" role="img" aria-label="Photo of a smiling couple taking a selfie in front of a domed cathedral and a TV tower">
  <div class="hero-title abs">DUIS QUAM NAM EGET LACUS ALIQUAM</div>
  <div class="hero-sub abs">PRAESENT VITAE LACUS VELIT VESTIBULUM</div>
  <div class="hero-dots abs"><span class="is-active"></span><span></span><span></span><span></span></div>
</section>

<a class="destination abs" style="left:65px">
  <div class="destination-photo" role="img" aria-label="Photo of a Gothic church under blue sky" style="background:linear-gradient(#3c6fc2,#a9bfd9 55%,#6f8a4f)"></div>
  <div class="destination-label">SPAIN &amp; PORTUGAL</div>
</a>
<a class="destination abs" style="left:237px">
  <div class="destination-photo" role="img" aria-label="Photo of a domed mausoleum at sunset" style="background:linear-gradient(#f0b23a,#e38a1e 60%,#8a4a1a)"></div>
  <div class="destination-label">INDIA</div>
</a>
<a class="destination abs" style="left:409px">
  <div class="destination-photo" role="img" aria-label="Photo of a hiker overlooking green cliffs" style="background:linear-gradient(#9fc3e6,#c6c4b0 40%,#6f8f45)"></div>
  <div class="destination-label">AFRICA</div>
</a>
<a class="destination abs" style="left:582px">
  <div class="destination-photo" role="img" aria-label="Photo of mountain peaks over a blue lake" style="background:linear-gradient(#c9774a,#6e6a74 45%,#2f6f8f)"></div>
  <div class="destination-label">SOUTH AMERICA</div>
</a>

<section class="welcome abs">
  <h1>Welcome to Our Website Mainpage</h1>
  <p class="welcome-lead">Morbi ornare gravida elit Integer congue augue et malesuada iaculis ipsum dui aliquet felis at cursus magna nisl nec elit Donec iaculis diam a nisi</p>
  <p class="welcome-body">Morbi ornare gravida elit Integer congue augue et malesuada iaculis ipsum dui aliquet felis at cursus magna nisl nec elit Donec iaculis diam a nisi accumsan viverra Duis sed tellus et tortor vestibulum gravida Praesent elementum elit at tellus Curabitur metus ipsum luctus eu malesuada ut tincidunt sed diam Maecenas at justo id velit placerat molestie Donec dictum lectus non odio Cras a ante vitae enim iaculis aliquam</p>
</section>

<aside class="deals abs">
  <h2>Travel Deals</h2>
  <p class="deals-link">Cursus magna nisl nec elit Donec iaculis diam a nisi accumsan viverra</p>
  <p class="deals-text">Duis sed tellus et tortor vestibulum gravida Praesent elementum elit at tellus Curabitur metus ipsum luctus eu malesuada ut tincidunt</p>
  <span class="button-gold">READ MORE</span>
</aside>

<div class="divider abs"></div>

<h2 class="testimonials-title abs">Testimonials</h2>

<div class="avatar abs" style="left:71px;top:851px" role="img" aria-label="Portrait of a customer"></div>
<blockquote class="quote abs" style="left:143px;top:848px">
  <span class="quote-mark">&ldquo;</span> Duis sed tellus et tortor vestibulum gravida Praesent elementum elit at tellus Curabitur metus ipsum luctus eu malesuada ut tincidunt sed diam Maecenas at justo id velit placerat molestie Donec dictum lectus non odio <span class="quote-mark">&rdquo;</span>
  <div class="quote-author">By Author Name</div>
</blockquote>

<div class="avatar abs" style="left:417px;top:851px" role="img" aria-label="Portrait of a customer"></div>
<blockquote class="quote abs" style="left:489px;top:848px">
  <span class="quote-mark">&ldquo;</span> Duis sed tellus et tortor vestibulum gravida Praesent elementum elit at tellus Curabitur metus ipsum luctus eu malesuada ut tincidunt sed diam Maecenas at justo id velit placerat molestie Donec dictum lectus non odio <span class="quote-mark">&rdquo;</span>
  <div class="quote-author">By Author Name</div>
</blockquote>

<footer class="site-footer abs"></footer>

<div class="footer-col abs" style="left:67px">
  <h3>Company</h3>
  <ul><li>About Company</li><li>Why Choose Us</li><li>How it works</li><li>Reviews Trips</li><li>Offers</li></ul>
</div>
<div class="footer-col abs" style="left:196px">
  <h3>Resources</h3>
  <ul><li>Tour Calender</li><li>Job Oppourtunities</li><li>Contact Us</li><li>Buy Travel Insurance</li></ul>
</div>
<div class="footer-col abs" style="left:325px">
  <h3>Special Offer</h3>
  <ul><li>Open an individual account</li><li>Open a business account</li><li>Other services</li><li>Refer a friend</li><li>Affiliates</li></ul>
</div>
<div class="footer-col abs" style="left:480px">
  <h3>Support</h3>
  <ul><li>FAQ</li><li>Customer Support</li><li>Resources</li><li>Advices &amp; Use</li><li>Contact</li></ul>
</div>
<div class="footer-col abs" style="left:600px">
  <h3>Newsletter Sign Up</h3>
  <p class="newsletter-note">Please subscribe here for latest offer</p>
  <div class="newsletter-input">email address</div>
  <div class="button-red">SUBSCRIBE</div>
  <div class="social" aria-label="Social media links"><span class="s-one"></span><span class="s-two"></span><span class="s-three"></span><span class="s-four"></span></div>
</div>

<div class="footer-base abs"></div>
<p class="copyright abs">&copy; 2014 Company Name&nbsp; All right reserved&nbsp; Term of Use</p>

</body>
</html>
```